Refresh of The Marston Collective business card

Update business card design using existing primary logo. Names, numbers, etc. are too hard to read on current design.

Target Market(s)

We are a CPA firm.

Industry/Entity Type

Accountant

Contact Information for Business Card

update current card

Colors
0355a3
3176b5
85acd3
0792cd

Requirements
Must have
• Easier to read phone numbers and names
• Use existing logo
Nice to have
• We love our color scheme and current TMC logo. But the names and phone numbers are too small and card just look old and stale.

```html
<!DOCTYPE html>
<html lang="en">
<head>
<meta charset="utf-8">
<title>The Marston Collective – Business Card</title>
<link rel="stylesheet" href="https://fonts.googleapis.com/css2?family=Cinzel:wght@600&family=Ubuntu:wght@400;500&display=swap">
<style>
  :root {
    --brand-navy: #0f2a5a;
    --brand-blue: #0355a3;
    --brand-bright: #2a66b4;
    --brand-mid: #3176b5;
    --ink: #3a3a3a;
    --tagline: #4a4a4a;
    --paper: #ffffff;
    --backdrop: #d9dadc;
  }
  * { margin: 0; padding: 0; box-sizing: border-box; }
  html, body { width: 1000px; height: 1200px; overflow: hidden; }
  body { background: var(--backdrop); position: relative; font-family: "Ubuntu", sans-serif; }

  .card {
    position: absolute;
    left: 78px;
    width: 823px;
    height: 503px;
    background: var(--paper);
    box-shadow: 0 10px 18px rgba(0,0,0,0.18);
    overflow: hidden;
  }
  .card--front { top: 46px; }
  .card--back  { top: 638px; }

  .band {
    position: absolute;
    left: 0; right: 0; bottom: 0;
    height: 77px;
    background: linear-gradient(90deg, var(--brand-navy) 0%, #1a3f7c 45%, var(--brand-bright) 100%);
    color: var(--paper);
    display: flex; align-items: center; justify-content: center;
  }
  .band__name {
    font-family: "Cinzel", serif;
    font-weight: 600;
    font-size: 29px;
    letter-spacing: 0.5px;
  }
  .band__web {
    font-family: "Ubuntu", sans-serif;
    font-weight: 500;
    font-size: 24px;
    letter-spacing: 0.4px;
  }

  .brand {
    position: absolute;
    display: flex;
    align-items: center;
  }
  .brand__dot {
    flex: none;
    border-radius: 50%;
    background: var(--brand-blue);
  }
  .brand__text { display: flex; flex-direction: column; }
  .brand__name {
    font-family: "Cinzel", serif;
    font-weight: 600;
    color: var(--brand-blue);
    line-height: 1.05;
  }
  .brand__tagline {
    font-family: "Ubuntu", sans-serif;
    font-weight: 500;
    color: var(--tagline);
    text-transform: uppercase;
  }

  .card--front .brand { left: 200px; top: 142px; gap: 22px; }
  .card--front .brand__dot { width: 140px; height: 140px; }
  .card--front .brand__name { font-size: 38px; }
  .card--front .brand__tagline { font-size: 11px; letter-spacing: 3px; margin-top: 12px; }

  .card--back .brand { left: 39px; top: 132px; gap: 18px; }
  .card--back .brand__dot { width: 110px; height: 110px; }
  .card--back .brand__name { font-size: 28px; }
  .card--back .brand__tagline { font-size: 8.5px; letter-spacing: 2.3px; margin-top: 9px; }

  .contacts {
    position: absolute;
    left: 426px;
    top: 124px;
    list-style: none;
    color: var(--ink);
    font-size: 22.5px;
    line-height: 1.3;
  }
  .contacts__item {
    display: flex;
    align-items: flex-start;
    margin-bottom: 9px;
  }
  .contacts__icon {
    flex: none;
    width: 24px; height: 24px;
    margin: 2px 14px 0 0;
    fill: var(--brand-blue);
  }
</style>
</head>
<body>

  <section class="card card--front">
    <div class="brand">
      <span class="brand__dot"></span>
      <div class="brand__text">
        <span class="brand__name">The Marston<br>Collective</span>
        <span class="brand__tagline">Certified Public Accountants</span>
      </div>
    </div>
    <div class="band">
      <span class="band__name">Daniel R. Marston, CPA</span>
    </div>
  </section>

  <section class="card card--back">
    <div class="brand">
      <span class="brand__dot"></span>
      <div class="brand__text">
        <span class="brand__name">The Marston<br>Collective</span>
        <span class="brand__tagline">Certified Public Accountants</span>
      </div>
    </div>

    <ul class="contacts">
      <li class="contacts__item">
        <svg class="contacts__icon" viewBox="0 0 24 24" aria-hidden="true"><path d="M12 1.5a7 7 0 0 0-7 7c0 5.2 7 14 7 14s7-8.8 7-14a7 7 0 0 0-7-7zm0 10a3 3 0 1 1 0-6 3 3 0 0 1 0 6z"/></svg>
        <span>318 N. Harlow Ave. Suite 204,<br>Winter Park, Florida 32789</span>
      </li>
      <li class="contacts__item">
        <svg class="contacts__icon" viewBox="0 0 24 24" aria-hidden="true"><path d="M15 2.5l3 4-2.4 2.4c-.6.6-.6 1.2-.3 2L14 14c-.6 1.2-1.8 2.5-3.4 3.4-.7.4-1.4.3-2-.3L6.2 19.5l4 3C15.5 21 19.5 14 19.5 7.5c0-2-1.3-3.8-4.5-5z"/></svg>
        <span>407.555.0142</span>
      </li>
      <li class="contacts__item">
        <svg class="contacts__icon" viewBox="0 0 24 24" aria-hidden="true"><path d="M6 2h12v5H6zM3 8h18a2 2 0 0 1 2 2v7h-4v5H5v-5H1v-7a2 2 0 0 1 2-2zm4 8v4h10v-4zm1 1h8v1H8z"/></svg>
        <span>407.555.0187</span>
      </li>
      <li class="contacts__item">
        <svg class="contacts__icon" viewBox="0 0 24 24" aria-hidden="true"><path d="M7 1h10a2 2 0 0 1 2 2v18a2 2 0 0 1-2 2H7a2 2 0 0 1-2-2V3a2 2 0 0 1 2-2zm0 3v14h10V4zm5 15.5a1.2 1.2 0 1 0 0 2.4 1.2 1.2 0 0 0 0-2.4z"/></svg>
        <span>407.555.0129</span>
      </li>
      <li class="contacts__item">
        <svg class="contacts__icon" viewBox="0 0 24 24" aria-hidden="true"><path d="M1 9h15v12H1zm1.5 1.5v.6l6 4.2 6-4.2v-.6zM18.5 2a4.5 4.5 0 1 1 0 9 4.5 4.5 0 0 1 0-9zm0 2.5a2 2 0 1 0 0 4 2 2 0 0 0 0-4z"/></svg>
        <span>dan@marstoncollective.com</span>
      </li>
    </ul>

    <div class="band">
      <span class="band__web">www.marstoncollective.com</span>
    </div>
  </section>

</body>
</html>
```